New lease of life for a tired Country Pub menu, QLD

I need to refresh my menus with updated prices. The menus need to be A4 (the menus are laminated and handed out over the bar. I'd like to include our logo. I will upload our existing menus as well as the new prices. The design should be humble yet stylish if that's ok, please

Target Market(s)

Locals, travellers and workers

Industry/Entity Type

Hospitality, Quintessential Country pub

Font styles to use
Sans Serif

Colors

Designer to choose colors to be used in the design.

Requirements
Must have
• as we run different menus on different nights
Nice to have
• our logo

```html
<!DOCTYPE html>
<html lang="en">
<head>
<meta charset="utf-8">
<title>Hotel Corvandale – Pizza Menu</title>
<link rel="stylesheet" href="https://fonts.googleapis.com/css2?family=Fira+Sans:wght@600;700;800&family=Montserrat:ital,wght@0,500;1,400&display=swap">
<style>
  :root {
    --backdrop: #b3b3b3;
    --card: #525252;
    --ink-light: #ffffff;
    --ink-dark: #4d4d4d;
    --shadow: rgba(0, 0, 0, 0.35);
  }
  * { margin: 0; padding: 0; box-sizing: border-box; }
  html, body {
    width: 890px; height: 1200px; overflow: hidden;
    background: var(--backdrop);
  }
  .menu-card {
    position: absolute; left: 72px; top: 72px;
    width: 747px; height: 1057px;
    background: var(--card);
    border-radius: 27px;
    overflow: hidden;
    box-shadow: 6px 8px 10px var(--shadow);
    color: var(--ink-light);
  }
  .venue-name {
    position: absolute; left: 0; right: 0; top: 43px;
    text-align: center;
    font-family: "Fira Sans", sans-serif; font-weight: 700;
    font-size: 21px; line-height: 23px; letter-spacing: 0.5px;
    color: var(--ink-light);
  }
  .menu-title {
    position: absolute; left: 0; right: 0; top: 127px;
    text-align: center;
    font-family: "Fira Sans", sans-serif; font-weight: 700;
    font-size: 46px; line-height: 48px;
  }
  .menu-sub {
    position: absolute; left: 0; right: 0; top: 171px;
    text-align: center;
    font-family: "Montserrat", sans-serif; font-weight: 500;
    font-size: 22px; line-height: 26px;
  }
  .menu-day {
    position: absolute; left: 304px; top: 200px;
    width: 139px; height: 17px; border-radius: 5px;
    background: var(--ink-light); color: var(--ink-dark);
    font-family: "Montserrat", sans-serif; font-weight: 500;
    font-size: 12px; line-height: 17px; text-align: center;
  }
  .pizza {
    position: absolute; left: 0; width: 747px; height: 60px;
  }
  .pizza-name {
    position: absolute; left: 40px; top: 5px;
    font-family: "Fira Sans", sans-serif; font-weight: 700;
    font-size: 25.5px; line-height: 28px;
  }
  .pizza-toppings {
    position: absolute; left: 40px; top: 35px; width: 555px;
    font-family: "Montserrat", sans-serif; font-style: italic; font-weight: 400;
    font-size: 11.3px; line-height: 14px;
  }
  .pizza-price {
    position: absolute; left: 608px; top: 0; width: 139px; height: 37px;
    background: var(--ink-light); color: var(--ink-dark);
    border-radius: 4px 0 0 4px;
    font-family: "Fira Sans", sans-serif; font-weight: 700;
    font-size: 31px; line-height: 37px; padding-left: 8px;
  }
  .footer-wave {
    position: absolute; left: 0; top: 980px; width: 747px; height: 77px;
  }
  .footer-note {
    position: absolute; left: 0; right: 0; top: 1014px;
    text-align: center;
    font-family: "Fira Sans", sans-serif; font-weight: 600;
    font-size: 16.5px; line-height: 19px; color: var(--ink-dark);
  }
</style>
</head>
<body>
  <main class="menu-card">
    <div class="venue-name">HOTEL<br>CORVANDALE</div>
    <h1 class="menu-title">PIZZA MENU</h1>
    <p class="menu-sub">Lunch &amp; Dinner</p>
    <p class="menu-day">Wednesdays Only</p>

    <section class="pizza" style="top:273px">
      <h2 class="pizza-name">BBQ SWEET CHILLI CHICKEN</h2>
      <p class="pizza-toppings">BBQ sauce with sweet chili sauce, cheddar cheese, mushrooms, onion, chicken, mozzarella</p>
      <div class="pizza-price">$24.50</div>
    </section>
    <section class="pizza" style="top:353px">
      <h2 class="pizza-name">HAWAIIAN</h2>
      <p class="pizza-toppings">Tomato sauce, cheddar cheese, Calder’s smoked ham and pineapple, mozzarella</p>
      <div class="pizza-price">$24.50</div>
    </section>
    <section class="pizza" style="top:433px">
      <h2 class="pizza-name">MEATLOVER’S</h2>
      <p class="pizza-toppings">BBQ sauce, cheddar cheese, seasoned mince, Calder’s smoked ham, beef sausage, mozzarella</p>
      <div class="pizza-price">$25.99</div>
    </section>
    <section class="pizza" style="top:512px">
      <h2 class="pizza-name">PEPPERONI</h2>
      <p class="pizza-toppings">Tomato sauce, cheddar cheese, pepperoni</p>
      <div class="pizza-price">$24.50</div>
    </section>
    <section class="pizza" style="top:592px">
      <h2 class="pizza-name">SUPREME</h2>
      <p class="pizza-toppings">Tomato sauce, cheddar cheese, Calder’s smoked ham, onion, capsicum, mushroom, pepperoni, pineapple, mozzarella olives</p>
      <div class="pizza-price">$25.99</div>
    </section>
    <section class="pizza" style="top:672px">
      <h2 class="pizza-name">TANDOORI CHICKEN</h2>
      <p class="pizza-toppings">Tomato/tandoori sauce, cheddar cheese, chicken, onion, capsicum, mozzarella</p>
      <div class="pizza-price">$24.50</div>
    </section>
    <section class="pizza" style="top:751px">
      <h2 class="pizza-name">VEGETARIAN</h2>
      <p class="pizza-toppings">Tomato sauce, cheddar cheese, onion, mushroom, capsicum, olives, pumpkin</p>
      <div class="pizza-price">$24.50</div>
    </section>

    <svg class="footer-wave" viewBox="0 0 747 77" aria-hidden="true">
      <path d="M15 72 Q373 -46 732 72 L747 77 L0 77 Z" fill="var(--ink-light)"/>
    </svg>
    <p class="footer-note">HALF/ HALF NOT AVAILABLE</p>
  </main>
</body>
</html>
```